Unique Concept Design to Website Needed

Please see the attached folder. I have random images,etc but most importantly I have an attached image I was working on as a concept of a website. The brown background with blue and brown squares. logo in upper left and a little about me and then the squares would have names on them to lead to a section of the website with more info. I envision, when you mouse over a square, an image would appear so I attached random images here as well. Maybe some squares already have some images too.
- I want simple fonts. i like CLEAN, fonts
- text should be minimal. i am changing my site to less text, more powerful, bolder, larger lines with less content
- i am not sold on brown as the secondary color. i like blue but maybe grays, whites, offwhite scales or some other colors
-i have another graphic in there too
-you can see from my mock what company i am. please feel free to look me up and pull any portfolio , info , etc content to help make a great mock.
Do something cool!

```html
<!DOCTYPE html>
<html lang="en">
<head>
<meta charset="utf-8">
<title>Brisk web studio, llc</title>
<link rel="stylesheet" href="https://fonts.googleapis.com/css2?family=Questrial&family=Open+Sans:wght@300;400&family=Arimo:wght@700&display=swap">
<style>
  :root {
    --bg-light: #d3d8c8;
    --bg-mid: #aab29d;
    --bg-dark: #7e8672;
    --teal-dark: #0f6b64;
    --teal-mid: #3f9a93;
    --teal-soft: #76b3ac;
    --tile-pale: #e6ebdf;
    --ink: #2f3a33;
    --logo-blue: #1d3a78;
    --grey-text: #5b5f58;
    --photo-dark: #2a2a1e;
    --photo-warm: #7a6a2e;
    --white: #ffffff;
    --icon: #141414;
  }
  * { box-sizing: border-box; margin: 0; padding: 0; }
  html, body { width: 1200px; height: 819px; overflow: hidden; }
  body { font-family: "Questrial", sans-serif; color: var(--ink); }

  .canvas { position: relative; width: 1200px; height: 819px; overflow: hidden; }
  .backdrop {
    position: absolute; inset: 0;
    background:
      linear-gradient(90deg, rgba(255,255,255,.25) 0%, rgba(255,255,255,0) 40%),
      radial-gradient(ellipse at 75% 60%, var(--bg-dark) 0%, var(--bg-mid) 45%, var(--bg-light) 100%);
  }

  .brand { position: absolute; left: 38px; top: 80px; }
  .brand-name { font-family: "Open Sans", sans-serif; font-weight: 300; font-size: 54px; color: var(--logo-blue); letter-spacing: -1px; line-height: 1; }
  .brand-tagline { font-family: "Open Sans", sans-serif; font-size: 13px; color: var(--grey-text); margin-top: 16px; }
  .intro { position: absolute; left: 85px; top: 206px; width: 330px; font-size: 14.5px; line-height: 21px; color: var(--grey-text); }

  .utility { position: absolute; right: 40px; top: 14px; display: flex; gap: 14px; }
  .social { position: absolute; right: 22px; bottom: 12px; display: flex; gap: 6px; }
  .social-item { width: 40px; height: 40px; border: 2px solid var(--white); display: flex; align-items: center; justify-content: center; color: var(--white); font-size: 10px; }

  .tile { position: absolute; opacity: .9; }
  .dark { background: var(--teal-dark); }
  .mid { background: var(--teal-mid); }
  .soft { background: var(--teal-soft); }
  .pale { background: var(--tile-pale); opacity: .75; }
  .r-tl { border-top-left-radius: 40%; }
  .r-tr { border-top-right-radius: 40%; }
  .r-bl { border-bottom-left-radius: 40%; }
  .r-br { border-bottom-right-radius: 40%; }

  .nav-label { position: absolute; font-size: 15px; color: var(--ink); line-height: 18px; }
  .nav-label.light { color: var(--white); }

  .portrait {
    position: absolute; left: 735px; top: 345px; width: 230px; height: 230px;
    border-radius: 38px; background: linear-gradient(160deg, #8a7a3c, #c9b56a 55%, #6f7a62);
    border: 2px solid rgba(255,255,255,.6);
  }
  .portrait::before, .portrait::after { content: ""; position: absolute; background: rgba(255,255,255,.6); }
  .portrait::before { left: 114px; top: 0; width: 2px; height: 100%; }
  .portrait::after { top: 114px; left: 0; height: 2px; width: 100%; }

  .feature-grid { position: absolute; left: 218px; top: 508px; width: 223px; height: 226px; display: grid; grid-template-columns: 110px 111px; grid-template-rows: 113px 111px; gap: 2px; }
  .feature { position: relative; background: linear-gradient(150deg, var(--photo-warm), var(--photo-dark)); font-family: "Arimo", sans-serif; font-weight: 700; color: var(--white); font-size: 16px; line-height: 20px; }
  .feature.round-br { border-bottom-right-radius: 40px; }
  .feature.round-tr { border-top-right-radius: 40px; }
  .feature-label { position: absolute; }
  .play { position: absolute; left: 28px; top: 24px; width: 64px; height: 64px; border: 1px solid var(--white); display: flex; align-items: center; justify-content: center; }
  .play-box { width: 32px; height: 32px; background: var(--white); display: flex; align-items: center; justify-content: center; }
</style>
</head>
<body>
<main class="canvas">
  <div class="backdrop" role="img" aria-label="Faded office interior with desk and chair, washed in sage green"></div>

  <header class="brand">
    <div class="brand-name">Brisk <span style="font-size:20px;letter-spacing:0">| web studio, llc</span></div>
    <p class="brand-tagline">Website Design.&nbsp; Website Support.&nbsp; Website Promotion.</p>
  </header>
  <p class="intro">Daniel Hartley is a digital marketing consultant developing and promoting websites , digital media and videos, for businesses</p>

  <nav class="utility" aria-label="Quick links">
    <svg width="38" height="34" viewBox="0 0 38 34" aria-label="Home"><path d="M19 2 2 18h5v14h9v-9h6v9h9V18h5z" fill="var(--icon)"/></svg>
    <svg width="44" height="34" viewBox="0 0 44 34" aria-label="Contact"><path d="M6 4c3-2 5 0 6 4s-1 4-2 5c1 4 4 8 8 10 1-1 2-3 5-2s5 3 3 6c-3 4-9 2-14-3S2 9 6 4z" fill="var(--icon)"/><rect x="22" y="6" width="20" height="13" fill="none" stroke="var(--icon)" stroke-width="2"/><path d="M22 6l10 7 10-7" fill="none" stroke="var(--icon)" stroke-width="2"/></svg>
    <svg width="24" height="34" viewBox="0 0 24 34" aria-label="Location"><path d="M12 2a9 9 0 0 0-9 9c0 8 9 21 9 21s9-13 9-21a9 9 0 0 0-9-9z" fill="var(--icon)"/><circle cx="12" cy="11" r="3.5" fill="var(--bg-light)"/></svg>
  </nav>

  <section class="tiles" aria-label="Site sections">
    <!-- top left small grid -->
    <div class="tile mid" style="left:428px;top:118px;width:30px;height:28px"></div>
    <div class="tile soft r-tr" style="left:460px;top:118px;width:28px;height:28px"></div>
    <div class="tile pale r-tl" style="left:495px;top:118px;width:55px;height:28px"></div>
    <div class="tile pale r-tr" style="left:555px;top:118px;width:58px;height:28px"></div>
    <div class="tile soft r-bl" style="left:428px;top:148px;width:30px;height:28px"></div>
    <div class="tile soft" style="left:460px;top:148px;width:28px;height:28px"></div>
    <div class="tile mid r-tl" style="left:490px;top:150px;width:60px;height:58px"></div>
    <div class="tile soft r-tl" style="left:553px;top:150px;width:58px;height:58px"></div>
    <div class="tile mid r-tr" style="left:614px;top:150px;width:58px;height:58px"></div>
    <div class="tile mid r-tl r-tr" style="left:620px;top:95px;width:110px;height:52px"></div>
    <div class="tile dark r-bl" style="left:676px;top:150px;width:55px;height:48px"></div>
    <div class="tile pale r-tl r-tr" style="left:750px;top:95px;width:96px;height:100px"></div>
    <!-- top right cluster -->
    <div class="tile dark r-tl" style="left:855px;top:150px;width:58px;height:60px"></div>
    <div class="tile soft r-tl" style="left:915px;top:120px;width:58px;height:28px"></div>
    <div class="tile dark r-br" style="left:915px;top:150px;width:58px;height:28px"></div>
    <div class="tile dark r-tr" style="left:975px;top:120px;width:58px;height:58px"></div>
    <div class="tile mid r-tr" style="left:1035px;top:155px;width:58px;height:58px"></div>
    <div class="tile pale r-bl" style="left:790px;top:160px;width:60px;height:52px"></div>
    <!-- second row -->
    <div class="tile mid r-bl" style="left:435px;top:222px;width:52px;height:52px"></div>
    <div class="tile mid r-br" style="left:490px;top:215px;width:58px;height:58px"></div>
    <div class="tile mid r-bl" style="left:553px;top:215px;width:58px;height:58px"></div>
    <div class="tile pale r-tl" style="left:617px;top:215px;width:58px;height:58px"></div>
    <div class="tile mid r-br" style="left:678px;top:215px;width:58px;height:58px"></div>
    <div class="tile dark r-tl" style="left:740px;top:215px;width:110px;height:55px"></div>
    <div class="tile soft r-tr" style="left:852px;top:215px;width:58px;height:55px"></div>
    <div class="tile mid r-tl" style="left:912px;top:215px;width:58px;height:55px"></div>
    <div class="tile pale r-tl r-tr" style="left:975px;top:215px;width:120px;height:115px"></div>
    <div class="tile pale" style="left:760px;top:272px;width:92px;height:55px"></div>
    <div class="tile mid r-br" style="left:856px;top:272px;width:112px;height:55px"></div>
    <!-- services block -->
    <div class="tile soft r-tl" style="left:555px;top:277px;width:60px;height:55px"></div>
    <div class="tile pale r-tl" style="left:618px;top:277px;width:55px;height:55px"></div>
    <div class="tile mid r-br" style="left:676px;top:277px;width:58px;height:55px"></div>
    <div class="tile dark r-bl" style="left:555px;top:335px;width:118px;height:52px"></div>
    <div class="tile pale r-tl" style="left:445px;top:285px;width:108px;height:52px"></div>
    <!-- left cluster -->
    <div class="tile mid r-tl" style="left:208px;top:328px;width:28px;height:26px"></div>
    <div class="tile mid" style="left:238px;top:328px;width:28px;height:26px"></div>
    <div class="tile soft r-bl" style="left:208px;top:356px;width:28px;height:26px"></div>
    <div class="tile soft" style="left:238px;top:356px;width:28px;height:26px"></div>
    <div class="tile mid r-tr" style="left:268px;top:328px;width:60px;height:54px"></div>
    <div class="tile mid r-tl" style="left:335px;top:285px;width:108px;height:52px"></div>
    <div class="tile soft r-bl" style="left:335px;top:340px;width:48px;height:50px"></div>
    <div class="tile pale r-tr" style="left:385px;top:340px;width:55px;height:50px"></div>
    <div class="tile pale r-tl" style="left:445px;top:340px;width:108px;height:48px"></div>
    <!-- media cluster -->
    <div class="tile mid r-tl" style="left:215px;top:395px;width:112px;height:55px"></div>
    <div class="tile soft r-bl" style="left:215px;top:452px;width:55px;height:52px"></div>
    <div class="tile mid" style="left:272px;top:452px;width:55px;height:52px"></div>
    <div class="tile mid r-tr" style="left:330px;top:395px;width:52px;height:52px"></div>
    <div class="tile soft r-bl" style="left:330px;top:450px;width:110px;height:55px"></div>
    <div class="tile mid r-tl r-tr" style="left:385px;top:395px;width:55px;height:52px"></div>
    <div class="tile pale r-tl" style="left:445px;top:395px;width:52px;height:52px"></div>
    <div class="tile pale r-br" style="left:500px;top:395px;width:52px;height:52px"></div>
    <div class="tile pale r-tl" style="left:445px;top:452px;width:52px;height:52px"></div>
    <div class="tile mid r-br" style="left:500px;top:455px;width:52px;height:50px"></div>
    <!-- right column -->
    <div class="tile mid r-tl" style="left:978px;top:345px;width:58px;height:52px"></div>
    <div class="tile mid r-tr" style="left:1038px;top:345px;width:52px;height:52px"></div>
    <div class="tile soft r-bl" style="left:978px;top:400px;width:58px;height:52px"></div>
    <div class="tile pale r-br" style="left:1038px;top:400px;width:52px;height:52px"></div>
    <div class="tile dark r-tl" style="left:975px;top:458px;width:58px;height:55px"></div>
    <div class="tile dark r-br" style="left:1035px;top:458px;width:55px;height:55px"></div>
    <div class="tile pale r-bl" style="left:975px;top:515px;width:58px;height:55px"></div>
    <div class="tile pale r-br" style="left:1035px;top:515px;width:55px;height:55px"></div>

    <a class="nav-label" style="left:678px;top:118px">design</a>
    <a class="nav-label light" style="left:764px;top:238px">portfolio</a>
    <a class="nav-label" style="left:999px;top:226px">free<br>resources</a>
    <a class="nav-label" style="left:620px;top:297px">services</a>
    <a class="nav-label" style="left:395px;top:352px">blog</a>
    <a class="nav-label light" style="left:278px;top:407px">media</a>
    <a class="nav-label light" style="left:986px;top:359px">pay<br>online</a>
  </section>

  <div class="portrait" role="img" aria-label="Portrait photo of the consultant in a warm office"></div>

  <section class="feature-grid" aria-label="Featured links">
    <div class="feature" role="img" aria-label="Video still of the studio workspace">
      <div class="play"><div class="play-box"><svg width="16" height="18" viewBox="0 0 16 18"><path d="M2 1l13 8-13 8z" fill="var(--icon)"/></svg></div></div>
    </div>
    <div class="feature round-br" role="img" aria-label="Photo of the studio at night"><span class="feature-label" style="left:22px;top:48px">about us</span></div>
    <div class="feature" role="img" aria-label="Photo of a desk with laptop"><span class="feature-label" style="left:22px;top:28px">from &nbsp;the<br>&nbsp;owner</span></div>
    <div class="feature round-tr" style="background:linear-gradient(150deg,#3a3320,#0d0d08)" role="img" aria-label="Dark photo of the office"><span class="feature-label" style="left:5px;top:50px">testimonials</span></div>
  </section>

  <nav class="social" aria-label="Social links">
    <span class="social-item">share</span>
    <span class="social-item">post</span>
    <span class="social-item">link</span>
    <span class="social-item">notes</span>
  </nav>
</main>
</body>
</html>
```